App Design - Job Poise Lantern

We require an App Design for our new App called 'Poise Lantern'. This app is essentially an assistant to help Users prepare for job interviews, to help them get hired. <br/><br/>Users who download the App can view common Questions and Answers, save their favourite responses and also view common Interview Tips. <br/><br/>The vision for our App is for Users who are preparing for an interview (1 week before, 1 day before, even 1 hour before), are able to download, view and educate themselves on common questions and responses, and then be confident to land the job. <br/><br/>Our team has developed wireframes to help highlight what each screen should do and include. Please see attached document, which also highlights key requirements for the experience. Feel free to add/remove/edit what you see on these wireframes. Our preference is that you use Adobe XD please.<br/><br/>In terms of design guidelines, we want the experience to be simple, intuitive and 'memorable' to help Users to remember the questions/responses when they are in the interview. <br/><br/>The final design should communicate 'neat and clean professionalism'; we like the design of: vocatia hub com au<br/><br/>Thank you for reading! Good luck !

Target Market(s)

Professional job seekers

Font styles to use
Sans Serif

Colors

Designer to choose colors to be used in the design.

Requirements
Must have
• Please see my PixelBazaar_UX file that I have uploaded
Nice to have
• Could you also please include some ideas on how we can incorporate Advertising into the app screens

```html
<!DOCTYPE html>
<html lang="en">
<head>
<meta charset="utf-8">
<title>Poise Lantern – Home</title>
<link rel="stylesheet" href="https://fonts.googleapis.com/css2?family=Montserrat:wght@700;800&family=Figtree:wght@400;500&display=swap">
<style>
  :root {
    --brand-blue: #1857d8;
    --brand-blue-deep: #1346b8;
    --icon-tint: #dbe5f8;
    --page-grey: #f3f3f3;
    --card-white: #ffffff;
    --ink: #111111;
    --on-blue: #ffffff;
  }
  * { margin: 0; padding: 0; box-sizing: border-box; }
  html, body { width: 1200px; height: 2598px; overflow: hidden; }
  body {
    position: relative;
    background: var(--page-grey);
    font-family: "Figtree", sans-serif;
    color: var(--ink);
  }
  .hero {
    position: absolute; left: 0; top: 0; width: 1200px; height: 818px;
    overflow: hidden;
    background: linear-gradient(160deg, #1a5fe6 0%, var(--brand-blue) 45%, var(--brand-blue-deep) 100%);
  }
  .hero-photo {
    position: absolute; inset: 0;
    background: radial-gradient(ellipse at 30% 55%, rgba(10,40,140,0.35), transparent 60%),
                radial-gradient(ellipse at 85% 50%, rgba(10,40,140,0.25), transparent 55%);
  }
  .hero-watermark {
    position: absolute; left: -100px; top: 170px; width: 1400px;
    font-family: "Montserrat", sans-serif; font-weight: 800;
    font-size: 205px; line-height: 172px; letter-spacing: 2px;
    color: rgba(255,255,255,0.07); white-space: nowrap; text-align: center;
  }
  .status-bar {
    position: absolute; left: 0; top: 0; width: 1200px; height: 116px;
    color: var(--on-blue);
  }
  .status-time {
    position: absolute; left: 40px; top: 32px;
    font-size: 42px; font-weight: 500;
  }
  .status-icons { position: absolute; right: 40px; top: 42px; }
  .app-title {
    position: absolute; left: 0; top: 240px; width: 1200px;
    text-align: center; color: var(--on-blue);
    font-family: "Montserrat", sans-serif; font-weight: 800;
    font-size: 62px; line-height: 80px; letter-spacing: 0.5px;
  }
  .menu-card {
    position: absolute; left: 48px; width: 1109px; height: 446px;
    background: var(--card-white); border-radius: 22px;
    box-shadow: 0 6px 24px rgba(0,0,0,0.06);
  }
  .menu-icon {
    position: absolute;
    background: var(--icon-tint);
    border-radius: 28px;
  }
  .menu-label {
    position: absolute; left: 0; width: 100%; text-align: center;
    font-size: 54px; font-weight: 400; color: var(--ink);
  }
</style>
</head>
<body>
  <header class="hero">
    <div class="hero-photo" role="img" aria-label="Blue-tinted photo of a candidate writing notes at a desk"></div>
    <div class="hero-watermark">POISE<br>LANTERN</div>
    <div class="status-bar">
      <span class="status-time">9:41</span>
      <svg class="status-icons" width="166" height="32" viewBox="0 0 166 32">
        <g fill="#fff">
          <rect x="0" y="20" width="7" height="10" rx="1.5"/>
          <rect x="11" y="15" width="7" height="15" rx="1.5"/>
          <rect x="22" y="9" width="7" height="21" rx="1.5"/>
          <rect x="33" y="3" width="7" height="27" rx="1.5"/>
          <path d="M72 30 l-6-7 a9 9 0 0 1 12 0z"/>
          <path d="M57 13 a21 21 0 0 1 30 0 l-4 4 a15 15 0 0 0 -22 0z"/>
          <rect x="108" y="4" width="50" height="24" rx="6" fill="none" stroke="#fff" stroke-width="2.5"/>
          <rect x="112" y="8" width="42" height="16" rx="3"/>
          <rect x="161" y="12" width="4" height="8" rx="1.5"/>
        </g>
      </svg>
    </div>
    <h1 class="app-title">POISE LANTERN</h1>
  </header>

  <main>
    <section class="menu-card" style="top:640px">
      <div class="menu-icon" style="left:464px;top:72px;width:182px;height:182px" role="img" aria-label="Blue line icon of two speech bubbles with a question mark"></div>
      <h2 class="menu-label" style="top:314px">View Questions &amp; Responses</h2>
    </section>

    <section class="menu-card" style="top:1213px">
      <div class="menu-icon" style="left:471px;top:92px;width:167px;height:167px" role="img" aria-label="Blue line icon of a profile document with a pencil"></div>
      <h2 class="menu-label" style="top:304px">My Question Portfolio</h2>
    </section>

    <section class="menu-card" style="top:1797px">
      <div class="menu-icon" style="left:455px;top:84px;width:198px;height:197px" role="img" aria-label="Blue line icon of two people talking across a table"></div>
      <h2 class="menu-label" style="top:318px">Interview Tips</h2>
    </section>
  </main>
</body>
</html>
```